We need a clean but professional business card design for a men's grooming barber shop. Our demographic is for the professional male so it needs to be esthetically pleasing and interesting to that demographic. Our website has a leather background and we have hardwood flooring in the shop so either of those two could work on the card.
I would not be apposed to a slightly different shape business card than usual, like a square.
The final design should be clean, clear, and call out to all male professionals looking for a guys place to get a cut and a shave and relax with a cigar.
Target Market(s)
Professional Male ages between 25 -50
Industry/Entity Type
Business
Requirements
Must have
- My logo and be visible. I designed myself some referral cards and i need to make the background of my logo have a white dropshadow.

```html
<!DOCTYPE html>
<html lang="en">
<head>
<meta charset="utf-8">
<title>Shavers of the Fernridge – Business Card</title>
<link rel="stylesheet" href="https://fonts.googleapis.com/css2?family=Open+Sans:wght@400;700&display=swap">
<style>
  :root {
    --canvas-bg: #e9e7e3;
    --card-bg: #3b3b3d;
    --card-motif: #4a4a4c;
    --card-ink: #ffffff;
    --card-shadow: rgba(0, 0, 0, 0.35);
  }
  * { margin: 0; padding: 0; box-sizing: border-box; }
  html, body {
    width: 1200px;
    height: 1000px;
    overflow: hidden;
    background: var(--canvas-bg);
    font-family: "Open Sans", Arial, sans-serif;
  }
  .canvas { position: relative; width: 1200px; height: 1000px; }

  .card {
    position: absolute;
    top: 233px;
    width: 302px;
    height: 542px;
    overflow: hidden;
    background: var(--card-bg);
    color: var(--card-ink);
    box-shadow: 0 2px 6px var(--card-shadow);
  }
  .card--front { left: 78px; }
  .card--back  { left: 437px; }

  .card__motif {
    position: absolute;
    inset: 0;
    background:
      radial-gradient(circle at 10% 18%, var(--card-motif) 0, rgba(74,74,76,0) 42%),
      radial-gradient(circle at 88% 78%, var(--card-motif) 0, rgba(74,74,76,0) 52%);
  }

  .brand {
    position: absolute;
    left: 0;
    width: 100%;
    display: flex;
    align-items: center;
    justify-content: center;
    gap: 12px;
    font-weight: 700;
    font-size: 22px;
    line-height: 26px;
    text-transform: uppercase;
    letter-spacing: 0.5px;
    color: var(--card-ink);
  }
  .brand__dot {
    width: 18px;
    height: 18px;
    border-radius: 50%;
    background: var(--card-ink);
    flex: none;
  }
  .card--front .brand { top: 151px; }
  .card--back  .brand { top: 106px; }

  .tagline {
    position: absolute;
    top: 428px;
    left: 0;
    width: 100%;
    text-align: center;
    font-size: 14.5px;
    line-height: 24px;
  }

  .contact { list-style: none; font-size: 13px; }
  .contact__item {
    position: absolute;
    left: 30px;
    display: flex;
    align-items: flex-start;
  }
  .contact__item--phone { top: 358px; }
  .contact__item--pin   { top: 402px; }
  .contact__item--web   { top: 438px; }
  .contact__item--home  { top: 477px; }
  .contact__icon {
    width: 22px;
    height: 20px;
    margin-right: 10px;
    flex: none;
  }
  .contact__text { line-height: 17px; padding-top: 1px; }
</style>
</head>
<body>
<main class="canvas">

  <section class="card card--front" aria-label="Card front">
    <div class="card__motif" role="img" aria-label="Faint oversized brand motif in the background"></div>
    <div class="brand"><span class="brand__dot"></span><span>Shavers of<br>the Fernridge</span></div>
    <p class="tagline">“Real Men don’t belong in a Salon,<br>They belong in a barber shop”</p>
  </section>

  <section class="card card--back" aria-label="Card back">
    <div class="card__motif" role="img" aria-label="Faint oversized brand motif in the background"></div>
    <div class="brand"><span class="brand__dot"></span><span>Shavers of<br>the Fernridge</span></div>
    <ul class="contact">
      <li class="contact__item contact__item--phone">
        <svg class="contact__icon" viewBox="0 0 22 20" aria-hidden="true">
          <rect x="7" y="2" width="9" height="16" rx="1.5" fill="none" stroke="#fff" stroke-width="1.6"/>
          <rect x="9" y="4.5" width="5" height="4" fill="#fff"/>
          <circle cx="11.5" cy="14.5" r="1" fill="#fff"/>
        </svg>
        <span class="contact__text">555.210.7391</span>
      </li>
      <li class="contact__item contact__item--pin">
        <svg class="contact__icon" viewBox="0 0 22 20" aria-hidden="true">
          <path d="M11 1a6 6 0 0 0-6 6c0 4.5 6 12 6 12s6-7.5 6-12a6 6 0 0 0-6-6z" fill="#fff"/>
          <circle cx="11" cy="7" r="2.3" fill="#3b3b3d"/>
        </svg>
        <span class="contact__text">N. 41d 08.220 W. 77d 36.514</span>
      </li>
      <li class="contact__item contact__item--web">
        <svg class="contact__icon" viewBox="0 0 22 20" aria-hidden="true">
          <g fill="none" stroke="#fff" stroke-width="1.3">
            <circle cx="11" cy="10" r="8.5"/>
            <ellipse cx="11" cy="10" rx="3.8" ry="8.5"/>
            <line x1="2.5" y1="10" x2="19.5" y2="10"/>
            <line x1="4" y1="5.5" x2="18" y2="5.5"/>
            <line x1="4" y1="14.5" x2="18" y2="14.5"/>
          </g>
        </svg>
        <span class="contact__text">www.shaversofthefernridge.com</span>
      </li>
      <li class="contact__item contact__item--home">
        <svg class="contact__icon" viewBox="0 0 22 20" aria-hidden="true">
          <path d="M11 2 2 10h3v8h12v-8h3z" fill="#fff"/>
          <rect x="9.2" y="12" width="3.6" height="6" fill="#3b3b3d"/>
        </svg>
        <span class="contact__text">42 Alder Court, Suite B<br>Marlow, OR 97201</span>
      </li>
    </ul>
  </section>

</main>
</body>
</html>
```